Business Card Design Project

We need a business card design for an existing company in Dallas/Fort Worth that is expanding services and re-branding. We are changing the name from Brightmoor Commercial Cleaning to Keystride Facility Services. We are expanding from only commercial cleaning to include complete commercial landscape and facility maintenance services, too.

As stated, we offer a package of services that includes landscape, janitorial and facility services, which is largely unique in the industry.

We would like a design that communicates trust/partnership with a professional, corporate image, but not necessarily using the standard white business card. We would like a design that perhaps uses darker blues or perhaps a gray background, but we are open to other ideas. We might also be interested in a double-sided design - maybe with our logo on the back, printed on a gray background?

We will probably stick with the attached logo, but if you've got another inspired idea....

Target Market(s)

Property managers, commercial real estate professionals, corporate executives

Industry/Entity Type

Landscape

Requirements
Should not have
• Not interested in old style fonts.

```html
<!DOCTYPE html>
<html lang="en">
<head>
<meta charset="utf-8">
<title>Keystride Facility Services – Business Card</title>
<link rel="stylesheet" href="https://fonts.googleapis.com/css2?family=Lato:wght@400;700&display=swap">
<style>
  :root {
    --navy: #0d3f73;
    --navy-dark: #0a3461;
    --ink: #2b2b2b;
    --white: #ffffff;
    --backdrop: #e4e8ea;
    --card-shadow: rgba(20, 40, 60, 0.18);
  }
  * { box-sizing: border-box; margin: 0; padding: 0; }
  html, body {
    width: 1200px; height: 960px; overflow: hidden;
    background: var(--backdrop);
    font-family: "Lato", Arial, sans-serif;
  }
  .canvas { position: relative; width: 1200px; height: 960px; }

  .card {
    position: absolute; left: 250px; width: 700px; height: 400px;
    box-shadow: 0 10px 30px var(--card-shadow);
    overflow: hidden;
  }
  .card--front { top: 60px; background: var(--white); }
  .card--back {
    top: 500px;
    background: linear-gradient(135deg, var(--navy) 0%, var(--navy-dark) 100%);
  }

  /* Company name set as plain text */
  .company {
    position: absolute; display: flex; align-items: center; gap: 14px;
    white-space: nowrap;
  }
  .company__dot {
    width: 26px; height: 26px; border-radius: 50%; background: currentColor; flex: none;
  }
  .company__name {
    font-size: 30px; font-weight: 400; letter-spacing: 2px; text-transform: uppercase;
    line-height: 1;
  }
  .card--front .company { top: 48px; left: 34px; color: var(--ink); }
  .card--back .company {
    top: 50%; left: 50%; transform: translate(-50%, -50%); color: var(--white);
  }

  /* Name band */
  .name-band {
    position: absolute; left: 0; right: 0; top: 130px; height: 100px;
    background: var(--navy); color: var(--white);
    padding: 24px 34px 0;
  }
  .name-band__name { font-size: 28px; font-weight: 400; letter-spacing: 0.5px; line-height: 1.1; }
  .name-band__title { font-size: 17px; margin-top: 8px; }

  /* Contact details */
  .contact { position: absolute; left: 34px; top: 292px; color: var(--ink); }
  .contact__lines { display: flex; gap: 22px; font-size: 19px; align-items: center; }
  .contact__item { display: flex; align-items: center; gap: 8px; }
  .contact__icon { width: 16px; height: 16px; fill: var(--navy); }
  .contact__web { margin-top: 10px; font-size: 18px; font-weight: 700; color: var(--navy); }

  .address {
    position: absolute; right: 34px; top: 262px; font-size: 16px; line-height: 1.55;
    color: var(--ink);
  }
</style>
</head>
<body>
<main class="canvas">

  <section class="card card--front" aria-label="Business card front">
    <div class="company">
      <span class="company__dot"></span>
      <span class="company__name">Keystride Facility Services</span>
    </div>

    <div class="name-band">
      <h1 class="name-band__name">MARISSA HOLLOWAY</h1>
      <p class="name-band__title">Director</p>
    </div>

    <div class="address">
      Level 4, 18 Harlow Street<br>
      PO Box 2260, Fairview 4410
    </div>

    <div class="contact">
      <div class="contact__lines">
        <span class="contact__item">
          <svg class="contact__icon" viewBox="0 0 16 16" aria-hidden="true">
            <path d="M3.5 1.5l2.5 0 1 3.5-1.6 1.2c.8 1.8 2.2 3.2 4 4l1.2-1.6 3.5 1v2.5c0 .8-.7 1.5-1.5 1.4C6.9 13 3 9.1 2.5 3c-.1-.8.6-1.5 1-1.5z"/>
          </svg>
          555-014-2290
        </span>
        <span class="contact__item">
          <svg class="contact__icon" viewBox="0 0 16 16" aria-hidden="true">
            <rect x="4" y="1" width="8" height="5"/>
            <rect x="1" y="6" width="14" height="7" rx="1"/>
            <rect x="4" y="11" width="8" height="4" fill="#fff" stroke="#0d3f73" stroke-width="1.2"/>
          </svg>
          555-014-2290
        </span>
      </div>
      <p class="contact__web">www.keystridefacilityservices.com</p>
    </div>
  </section>

  <section class="card card--back" aria-label="Business card back">
    <div class="company">
      <span class="company__dot"></span>
      <span class="company__name">Keystride Facility Services</span>
    </div>
  </section>

</main>
</body>
</html>
```